Velunor chemicals

We need a clean web design for a new e-commerce site selling Natural bio degrader products , please see attached docs

Industry/Entity Type

Graphic Design

```html
<!DOCTYPE html>
<html lang="en">
<head>
<meta charset="utf-8">
<title>Velunor chemicals</title>
<link rel="stylesheet" href="https://fonts.googleapis.com/css2?family=Open+Sans:ital,wght@0,400;0,600;0,700;1,400&display=swap">
<style>
:root{
  --blue:#0aa8d4;
  --blue-deep:#1a7dc0;
  --navy:#12609f;
  --brand:#1f6fb5;
  --green:#7ab800;
  --text:#555;
  --heading:#333;
  --muted:#888;
  --band:#f2f3f3;
  --footer-bar:#c8c9cb;
  --line:#cfd3d6;
}
*{box-sizing:border-box;margin:0;padding:0}
html,body{width:954px;height:1200px;overflow:hidden;background:#fff}
body{font-family:"Open Sans",Arial,sans-serif;color:var(--text);position:relative}
.abs{position:absolute}
a{color:inherit;text-decoration:none}

/* header */
.brand{left:162px;top:44px;display:flex;align-items:center;gap:8px;font-size:30px;font-weight:600;color:var(--brand);letter-spacing:1px}
.brand-dot{width:18px;height:18px;border-radius:50%;background:var(--blue)}
.cart{left:710px;top:18px;display:flex;gap:4px;font-size:8px;color:#222;line-height:12px;text-align:right}
.cart svg{margin-top:2px}
.call{left:612px;top:59px;display:flex;align-items:center;gap:8px;font-size:15px;color:#444}
.call b{color:var(--blue);font-weight:400}

/* nav */
.nav{left:162px;top:103px;width:630px;height:24px;border:1px solid var(--line);display:flex;justify-content:center;gap:30px;font-size:9.5px;color:#333;align-items:center;padding-right:40px}
.nav .active{color:var(--blue);border-bottom:1px solid var(--blue);padding-bottom:1px}

/* hero */
.hero{left:162px;top:131px;width:630px;height:256px;overflow:hidden}
.hero-photo{position:absolute;left:0;top:0;width:400px;height:256px;background:linear-gradient(135deg,#d9d9d6 0%,#b9a48a 45%,#9a7650 75%,#5d5f7e 100%)}
.hero-panel{position:absolute;inset:0}
.hero-title{position:absolute;right:57px;top:48px;font-size:17px;font-weight:600;color:#fff;white-space:nowrap}
.hero-copy{position:absolute;right:57px;top:87px;width:180px;text-align:right;font-size:9.8px;line-height:16.2px;color:#e8f7fc}
.btn-shop{position:absolute;left:436px;top:169px;width:123px;height:35px;background:var(--navy);color:#fff;font-size:16px;font-weight:600;display:flex;align-items:center;justify-content:center;border-radius:2px}
.dots{position:absolute;left:298px;top:239px;display:flex;gap:3px}
.dots i{width:6px;height:6px;border-radius:50%;background:#ccd2d6}
.dots i.on{background:var(--blue)}
.hero-shadow{left:162px;top:387px;width:630px;height:22px;background:radial-gradient(ellipse at top,rgba(0,0,0,.16),rgba(0,0,0,0) 70%)}

/* categories */
.cat-title{left:162px;top:446px;width:110px;height:35px;background:var(--blue-deep);color:#fff;font-size:16px;font-weight:600;display:flex;align-items:center;justify-content:center}
.cat-list{left:168px;top:489px;list-style:none;font-size:12.5px;color:#555}
.cat-list li{height:30.5px;display:flex;align-items:center;gap:6px}
.cat-list li::before{content:"";border-left:4px solid #777;border-top:3px solid transparent;border-bottom:3px solid transparent}
.see-all{left:760px;top:446px;font-size:11px;color:var(--brand)}

/* products */
.card{width:118px;height:110px;border:2px solid var(--blue);background:#fff}
.card-img{height:76px;margin:4px 18px 0;background:linear-gradient(90deg,#3f7fc2 0%,#cfe0ef 50%,#8fb6dd 100%);border-radius:6px 6px 2px 2px}
.card-img.pink{background:linear-gradient(90deg,#d2458f 0%,#f5d4e6 50%,#e9a3c8 100%)}
.card-img.orange{background:linear-gradient(90deg,#e9772c 0%,#fbe1cd 50%,#f2b58c 100%)}
.card-bar{position:absolute;left:-2px;right:-2px;bottom:-2px;height:28px;background:var(--green);display:flex;align-items:center}
.card-label{flex:1;padding-left:10px;font-size:10.5px;color:#222;white-space:nowrap}
.card-add{flex:0 0 31px;height:28px;background:var(--blue-deep);display:flex;align-items:center;justify-content:center}
.pager{left:751px;top:771px;display:flex;gap:6px}

/* newsletter */
.news{left:0;top:865px;width:954px;height:76px;background:var(--band)}
.news-text{left:174px;top:886px;font-size:17px;line-height:23px;color:var(--brand)}
.news-form{left:526px;top:891px;width:255px;height:32px;border:2px solid var(--blue);display:flex;background:#fff}
.news-input{flex:1;font-size:11px;font-style:italic;color:#8fc9e2;padding:6px 0 0 24px}
.news-go{flex:0 0 42px;border-left:2px solid var(--blue);display:flex;align-items:center;justify-content:center}

/* footer */
.f-head{top:990px;font-size:16px;color:var(--heading);font-weight:400}
.f-about{left:232px;top:1029px;width:165px;font-size:9.5px;line-height:14.5px;color:#444}
.f-links{left:459px;top:1029px;list-style:none;font-size:9px;line-height:16.3px;color:var(--muted)}
.f-contact{left:598px;top:1026px;list-style:none;font-size:9.5px;color:#555}
.f-contact li{height:21.3px;display:flex;align-items:center;gap:12px}
.f-contact .ic{width:12px;display:flex;justify-content:center}
.bottom{left:0;top:1164px;width:954px;height:36px;background:var(--footer-bar)}
.copy{left:162px;top:1174px;font-size:10.5px;color:#444}
.social{left:712px;top:1175px;display:flex;gap:8px}
.social i{width:13px;height:13px;border-radius:50%;background:var(--blue-deep)}
</style>
</head>
<body>

<header>
  <div class="abs brand"><span>VELUNOR</span><span class="brand-dot"></span></div>
  <div class="abs cart">
    <svg width="18" height="22" viewBox="0 0 18 22"><path d="M5 6V4a4 4 0 0 1 8 0v2" fill="none" stroke="#0aa8d4" stroke-width="1.6"/><rect x="1" y="6" width="16" height="15" rx="1" fill="#0aa8d4"/></svg>
    <div>Shopping Bag:<br>0 Items - $0.00<br>View Bag &amp; Checkout</div>
  </div>
  <div class="abs call">
    <svg width="32" height="32" viewBox="0 0 32 32"><circle cx="16" cy="16" r="14.5" fill="none" stroke="#0aa8d4" stroke-width="2"/><path d="M11 8.5l3 .2 1.2 4-2 1.4c1 2.3 2.6 3.9 4.7 4.8l1.5-2 4 1.2.1 3c-.3 1-1.3 1.6-2.4 1.5C14.3 22 9.9 17.6 9.4 11c-.1-1.2.6-2.2 1.6-2.5z" fill="#0aa8d4"/></svg>
    <span><b>Call Us</b> 012-555-0190</span>
  </div>
  <nav class="abs nav">
    <a class="active" href="#">HOME</a><a href="#">PRODUCTS</a><a href="#">ABOUT US</a><a href="#">SERVICES</a><a href="#">Contact US</a>
  </nav>
</header>

<section class="abs hero">
  <div class="hero-photo" role="img" aria-label="Photo of a person wiping an office desk with a cleaning spray bottle"></div>
  <svg class="hero-panel" width="630" height="256" viewBox="0 0 630 256"><polygon points="329,0 630,0 630,256 339,256 392,146" fill="#0aa8d4"/></svg>
  <div class="hero-title">Pellentesque accumsan</div>
  <p class="hero-copy">Lorem ipsum is a dummy text only. Dolor sit amet, consectetur adipiscing elit. Nullam felis mauris, eleifend ac rhoncus non,</p>
  <a class="btn-shop" href="#">Shop Now</a>
  <div class="dots"><i></i><i class="on"></i><i></i><i></i></div>
</section>
<div class="abs hero-shadow"></div>

<aside>
  <div class="abs cat-title">Categories</div>
  <ul class="abs cat-list">
    <li>Pellentesque</li><li>Accumsan</li><li>Dignissim</li><li>Libero eu</li><li>Dignissim</li><li>Aliquam sed</li><li>Accumsan</li>
  </ul>
</aside>

<a class="abs see-all" href="#">See all</a>

<section class="products">
  <div class="abs card" style="left:345px;top:479px"><div class="card-img" role="img" aria-label="Blue product bottles"></div><div class="card-bar"><span class="card-label">Lorem Ipsum</span><span class="card-add"><svg width="16" height="13" viewBox="0 0 16 13"><path d="M1 5h14l-2 7H3z" fill="none" stroke="#fff" stroke-width="1.4"/><path d="M5 5l3-4M11 5L9 2" stroke="#fff" stroke-width="1.4"/></svg></span></div></div>
  <div class="abs card" style="left:483px;top:479px"><div class="card-img pink" role="img" aria-label="Pink product bottles"></div><div class="card-bar"><span class="card-label">Lorem Ipsum</span><span class="card-add"><svg width="16" height="13" viewBox="0 0 16 13"><path d="M1 5h14l-2 7H3z" fill="none" stroke="#fff" stroke-width="1.4"/><path d="M5 5l3-4M11 5L9 2" stroke="#fff" stroke-width="1.4"/></svg></span></div></div>
  <div class="abs card" style="left:619px;top:479px"><div class="card-img orange" role="img" aria-label="Orange product bottles"></div><div class="card-bar"><span class="card-label">Lorem Ipsum</span><span class="card-add"><svg width="16" height="13" viewBox="0 0 16 13"><path d="M1 5h14l-2 7H3z" fill="none" stroke="#fff" stroke-width="1.4"/><path d="M5 5l3-4M11 5L9 2" stroke="#fff" stroke-width="1.4"/></svg></span></div></div>
  <div class="abs card" style="left:345px;top:626px"><div class="card-img" role="img" aria-label="Blue product bottles"></div><div class="card-bar"><span class="card-label">Lorem Ipsum</span><span class="card-add"><svg width="16" height="13" viewBox="0 0 16 13"><path d="M1 5h14l-2 7H3z" fill="none" stroke="#fff" stroke-width="1.4"/><path d="M5 5l3-4M11 5L9 2" stroke="#fff" stroke-width="1.4"/></svg></span></div></div>
  <div class="abs card" style="left:483px;top:626px"><div class="card-img pink" role="img" aria-label="Pink product bottles"></div><div class="card-bar"><span class="card-label">Lorem Ipsum</span><span class="card-add"><svg width="16" height="13" viewBox="0 0 16 13"><path d="M1 5h14l-2 7H3z" fill="none" stroke="#fff" stroke-width="1.4"/><path d="M5 5l3-4M11 5L9 2" stroke="#fff" stroke-width="1.4"/></svg></span></div></div>
  <div class="abs card" style="left:619px;top:626px"><div class="card-img orange" role="img" aria-label="Orange product bottles"></div><div class="card-bar"><span class="card-label">Lorem Ipsum</span><span class="card-add"><svg width="16" height="13" viewBox="0 0 16 13"><path d="M1 5h14l-2 7H3z" fill="none" stroke="#fff" stroke-width="1.4"/><path d="M5 5l3-4M11 5L9 2" stroke="#fff" stroke-width="1.4"/></svg></span></div></div>
  <div class="abs pager">
    <svg width="17" height="17" viewBox="0 0 17 17"><circle cx="8.5" cy="8.5" r="8" fill="#c9cccf"/><path d="M10 4.5L6 8.5l4 4M6 8.5h6" fill="none" stroke="#fff" stroke-width="1.8"/></svg>
    <svg width="17" height="17" viewBox="0 0 17 17"><circle cx="8.5" cy="8.5" r="8" fill="#1a6fb0"/><path d="M7 4.5l4 4-4 4M11 8.5H5" fill="none" stroke="#fff" stroke-width="1.8"/></svg>
  </div>
</section>

<section>
  <div class="abs news"></div>
  <p class="abs news-text">Sign up to our newsletter and receive<br>discounts and special offers</p>
  <div class="abs news-form"><span class="news-input">Enter email address</span><span class="news-go"><svg width="18" height="18" viewBox="0 0 18 18"><circle cx="9" cy="9" r="8.5" fill="#1a6fb0"/><path d="M8 5l4 4-4 4M12 9H5" fill="none" stroke="#fff" stroke-width="1.8"/></svg></span></div>
</section>

<footer>
  <h3 class="abs f-head" style="left:231px">About Velunor</h3>
  <h3 class="abs f-head" style="left:458px">Quick Links</h3>
  <h3 class="abs f-head" style="left:610px">Contact Us</h3>
  <p class="abs f-about">Lorem ipsum is a dummy text only. Dolor sit amet, consectetur adipiscing elit. Nullam felis mauris, eleifend ac rhoncus non, lobortis at diam.</p>
  <ul class="abs f-links"><li>HOME</li><li>LADIES</li><li>MENS</li><li>KIDS</li><li>Gallery</li><li>Contact US</li></ul>
  <ul class="abs f-contact">
    <li><span class="ic"><svg width="11" height="10" viewBox="0 0 11 10"><path d="M5.5 0L0 5h1.5v5h3V7h2v3h3V5H11z" fill="#1a7dc0"/></svg></span>Plant B. Manager</li>
    <li><span class="ic"></span>14 Larkfield Row</li>
    <li><span class="ic"></span>Ashbury, AB1 2CD</li>
    <li><span class="ic"><svg width="6" height="10" viewBox="0 0 6 10"><rect x=".7" y=".7" width="4.6" height="8.6" rx="1" fill="none" stroke="#1a7dc0" stroke-width="1.3"/></svg></span>0845 000 2231</li>
    <li><span class="ic"><svg width="11" height="8" viewBox="0 0 11 8"><rect width="11" height="8" fill="#1a7dc0"/><path d="M0 0l5.5 4.5L11 0" fill="none" stroke="#fff" stroke-width="1"/></svg></span>contact@example.com</li>
  </ul>
  <div class="abs bottom"></div>
  <p class="abs copy">Copyright©Velunor. All Rights Reserved. 2014</p>
  <div class="abs social"><i></i><i></i><i></i><i></i></div>
</footer>

</body>
</html>
```